Postcard Design Project

Dental Practice Name: Marlow Ridge Dental (logo)Phone Number (310-555-0147) Front and backAddress (7815 N. Harwick Ave. Ste. B, Culver City, CA, 90230. (Back side only)General, Cosmetic, and Implant Dentistry Mention: Emergencies/Walk-ins Welcome, "Hablamos Espanol", Open Weekends Front Side:Promotions: 1. $75 New Patient Special including Exam, X-Rays, and Cleaning 2. Free Consultation 3. Accept all PPO Insurances Services: 1. Implant ($800) + Implant Crown/Abutment ($1200) -use photo of missing tooth 2. Clear Braces (starting at $2900) -use picture of clearvona teeth, cut out everything else and just use the before and after of the clearvona pictures 3. Whitening ($95) -use pic of whitened teeth 4. White fillings (starting at $95) -use pic of silver to white fillings) Back Side: 1. Picture of practice 2. picture of map with pin location 3. address and phone number
Dental

```html
<!DOCTYPE html>
<html lang="en">
<head>
<meta charset="utf-8">
<title>Marlow Ridge Dental Postcard</title>
<link rel="stylesheet" href="https://fonts.googleapis.com/css2?family=Roboto+Condensed:ital,wght@0,400;0,700;1,400;1,700&family=Oswald:wght@500;600&display=swap">
<style>
  :root {
    --teal-band: #4fae9e;
    --teal-dark: #1c6f74;
    --teal-mid: #2a9c8c;
    --accent-red: #e2452f;
    --white: #ffffff;
    --page: #ffffff;
  }
  * { box-sizing: border-box; margin: 0; padding: 0; }
  html, body { width: 919px; height: 1200px; overflow: hidden; background: var(--page); }
  body { position: relative; font-family: "Roboto Condensed", Arial, sans-serif; color: var(--teal-dark); }

  .card { position: absolute; left: 50px; width: 820px; overflow: hidden; background: var(--white); }
  .card-front { top: 32px; height: 540px; }
  .card-back { top: 604px; height: 530px; }
  .abs { position: absolute; }

  /* Front */
  .front-hero { left: 0; top: 0; width: 820px; height: 392px;
    background: linear-gradient(90deg, #6f8f55 0%, #a7b878 30%, #e8e6b4 55%, #f5efc8 80%, #f2e6b0 100%); }
  .couple-photo { left: 0; top: 0; width: 440px; height: 392px;
    background: radial-gradient(ellipse at 45% 55%, #c99a7c 0%, #b98566 35%, rgba(160,170,110,0) 75%); }
  .brand { display: flex; align-items: center; gap: 10px; white-space: nowrap; }
  .brand-dot { width: 18px; height: 18px; border-radius: 50%; background: var(--teal-mid); flex: none; }
  .brand-name { font-family: "Roboto Condensed", Arial, sans-serif; font-weight: 400; color: var(--teal-mid); line-height: 1; white-space: nowrap; }
  .front-brand { left: 404px; top: 38px; }
  .front-brand .brand-name { font-size: 44px; }
  .tagline { font-family: "Oswald", Arial, sans-serif; font-weight: 600; font-size: 16px; letter-spacing: .2px; color: var(--teal-dark); white-space: nowrap; }
  .front-tagline { left: 454px; top: 95px; }
  .cta { font-style: italic; font-weight: 700; color: var(--teal-mid); }
  .front-cta { left: 454px; width: 350px; top: 133px; text-align: center; font-size: 19px; }
  .phone { font-family: "Oswald", Arial, sans-serif; font-weight: 600; color: var(--teal-dark); letter-spacing: .5px; }
  .front-phone { left: 454px; width: 350px; top: 156px; text-align: center; font-size: 42px; }

  .perks { left: 455px; top: 232px; list-style: none; }
  .perks li { display: flex; gap: 10px; font-family: "Oswald", Arial, sans-serif; font-weight: 500; font-size: 17px; line-height: 21px; color: var(--teal-dark); margin-bottom: 4px; }
  .perks li svg { flex: none; margin-top: 4px; }
  .perks .lang { color: var(--accent-red); }

  .special { left: 668px; top: 238px; width: 126px; height: 138px; border: 3px dotted var(--teal-mid); border-radius: 10px;
    background: rgba(255,255,255,.55); text-align: center; padding-top: 6px; }
  .special-price { font-family: "Oswald", Arial, sans-serif; font-weight: 600; font-size: 40px; line-height: 44px; color: var(--teal-dark); }
  .special-title { font-family: "Oswald", Arial, sans-serif; font-weight: 500; font-size: 13px; line-height: 16px; color: var(--accent-red); }
  .special-title.big { font-size: 17px; letter-spacing: 2px; line-height: 20px; }
  .special-items { font-size: 13px; line-height: 16px; color: var(--teal-dark); margin-top: 2px; }

  .services { left: 0; top: 392px; width: 820px; height: 148px; background: var(--teal-band); display: flex; }
  .service { position: relative; height: 100%; border-right: 2px solid var(--white); }
  .service:last-child { border-right: none; }
  .svc-implant { width: 207px; }
  .svc-braces { width: 211px; }
  .svc-whitening { width: 197px; }
  .svc-fillings { width: 205px; }
  .svc-title { font-family: "Oswald", Arial, sans-serif; font-weight: 600; color: var(--white); line-height: 1.05; }
  .svc-title small { font-size: 15px; }
  .implant-diagram { left: 18px; top: 14px; width: 80px; height: 122px; border-radius: 4px;
    background: linear-gradient(180deg, #e8f2f1 0%, #b9c7c6 50%, #7f8d8c 100%); opacity: .85; }
  .implant-text { left: 108px; top: 10px; font-size: 18px; }
  .implant-text .gap { display: block; height: 10px; }
  .braces-text { left: 0; width: 100%; top: 10px; text-align: center; font-size: 19px; }
  .photo-frame { background: var(--white); padding: 4px; }
  .braces-photo { left: 22px; top: 62px; width: 168px; height: 72px; }
  .whiten-text { left: 0; width: 100%; top: 16px; text-align: center; font-size: 20px; }
  .whiten-photo { left: 16px; top: 62px; width: 170px; height: 72px; }
  .fill-text { left: 12px; top: 12px; font-size: 19px; }
  .fill-photo { left: 106px; top: 24px; width: 88px; height: 100px; }
  .teeth-img { width: 100%; height: 100%; background: linear-gradient(180deg, #c2554a 0%, #f1ece0 40%, #faf7ee 60%, #c2554a 100%); }

  /* Back */
  .back-hero { left: 0; top: 0; width: 820px; height: 230px;
    background: radial-gradient(circle at 20% 40%, #ffffff 0%, #e6f0f3 40%, #cfe2e8 100%); }
  .back-brand { left: 20px; top: 30px; }
  .back-brand .brand-name { font-size: 46px; }
  .back-tagline { left: 102px; top: 90px; font-size: 15px; }
  .back-phone { left: 90px; width: 320px; top: 118px; text-align: center; font-size: 46px; }
  .back-cta { left: 90px; width: 320px; top: 186px; text-align: center; font-size: 19px; font-weight: 400; color: var(--teal-dark); }
  .welcome { left: 459px; top: 38px; width: 300px; font-style: italic; font-size: 20px; line-height: 27px; color: var(--teal-mid); white-space: nowrap; }
  .promo { left: 459px; top: 116px; font-size: 18px; line-height: 24px; color: var(--teal-mid); white-space: nowrap; }
  .seniors-photo { left: 612px; top: 92px; width: 202px; height: 138px;
    background: radial-gradient(ellipse at 50% 60%, #7a4c38 0%, #a76c58 40%, rgba(230,180,190,.6) 70%, rgba(207,226,232,0) 100%); }
  .location { left: 0; top: 230px; width: 820px; height: 60px; background: var(--teal-band);
    display: flex; align-items: center; gap: 36px; padding-left: 32px;
    font-family: "Oswald", Arial, sans-serif; font-weight: 600; font-size: 22px; color: var(--white); white-space: nowrap; }
  .map { left: 0; top: 290px; width: 423px; height: 240px; background: linear-gradient(135deg, #e6e6e3 0%, #dcdcd8 100%); }
  .office-photo { left: 423px; top: 290px; width: 397px; height: 240px;
    background: linear-gradient(180deg, #bfd6ea 0%, #dce8ef 28%, #c9744e 42%, #e7d3b0 60%, #9a9f8f 85%, #b7b7b2 100%); }
</style>
</head>
<body>

<section class="card card-front">
  <div class="abs front-hero" role="img" aria-label="Soft sunlit park background"></div>
  <div class="abs couple-photo" role="img" aria-label="Photo of a smiling couple embracing outdoors"></div>

  <div class="abs brand front-brand">
    <span class="brand-dot"></span>
    <span class="brand-name">Marlow Ridge Dental</span>
  </div>
  <div class="abs tagline front-tagline">GENERAL, COSMETIC, AND IMPLANT DENTISTRY</div>
  <div class="abs cta front-cta">Make an appointment today!</div>
  <div class="abs phone front-phone">310-555-0147</div>

  <ul class="abs perks">
    <li><svg width="14" height="12" viewBox="0 0 14 12"><path d="M1 6 L5 10 L13 1" fill="none" stroke="#1c6f74" stroke-width="2"/></svg><span>Emergencies &amp;<br>Walk-ins Welcome</span></li>
    <li><svg width="14" height="12" viewBox="0 0 14 12"><path d="M1 6 L5 10 L13 1" fill="none" stroke="#1c6f74" stroke-width="2"/></svg><span>All PPO plans accepted</span></li>
    <li><svg width="14" height="12" viewBox="0 0 14 12"><path d="M1 6 L5 10 L13 1" fill="none" stroke="#1c6f74" stroke-width="2"/></svg><span>Free consultation</span></li>
    <li><svg width="14" height="12" viewBox="0 0 14 12"><path d="M1 6 L5 10 L13 1" fill="none" stroke="#1c6f74" stroke-width="2"/></svg><span>Open Weekends</span></li>
    <li class="lang"><svg width="14" height="12" viewBox="0 0 14 12"><path d="M1 6 L5 10 L13 1" fill="none" stroke="#e2452f" stroke-width="2"/></svg><span>Hablamos Español</span></li>
  </ul>

  <div class="abs special">
    <div class="special-price">$75</div>
    <div class="special-title">NEW PATIENT</div>
    <div class="special-title big">SPECIAL</div>
    <div class="special-items">EXAM, X-RAYS,<br>AND CLEANING</div>
  </div>

  <div class="abs services">
    <div class="service svc-implant">
      <div class="abs implant-diagram" role="img" aria-label="Diagram of a dental implant with crown, abutment and implant post"></div>
      <div class="abs svc-title implant-text">IMPLANT<br>$800<span class="gap"></span>Crown +<br>Abutment<br>$1,200</div>
    </div>
    <div class="service svc-braces">
      <div class="abs svc-title braces-text">CLEAR BRACES<br><small>from</small> $2,900</div>
      <div class="abs photo-frame braces-photo"><div class="teeth-img" role="img" aria-label="Before and after photos of teeth straightened with clear aligners"></div></div>
    </div>
    <div class="service svc-whitening">
      <div class="abs svc-title whiten-text">WHITENING $95</div>
      <div class="abs photo-frame whiten-photo"><div class="teeth-img" role="img" aria-label="Before and after photos of whitened teeth"></div></div>
    </div>
    <div class="service svc-fillings">
      <div class="abs svc-title fill-text">White<br>FILLINGS<br><small>from</small> $95</div>
      <div class="abs photo-frame fill-photo"><div class="teeth-img" role="img" aria-label="Photos of silver fillings replaced with white fillings"></div></div>
    </div>
  </div>
</section>

<section class="card card-back">
  <div class="abs back-hero" role="img" aria-label="Soft light blue bokeh background"></div>

  <div class="abs brand back-brand">
    <span class="brand-dot"></span>
    <span class="brand-name">Marlow Ridge Dental</span>
  </div>
  <div class="abs tagline back-tagline">GENERAL, COSMETIC, AND IMPLANT DENTISTRY</div>
  <div class="abs phone back-phone">310-555-0147</div>
  <div class="abs cta back-cta">Call for an appointment today!</div>

  <div class="abs seniors-photo" role="img" aria-label="Photo of a smiling older couple"></div>
  <div class="abs welcome">Todos bienvenidos! Si no tiene<br>cita, no hay problema.</div>
  <div class="abs promo">PROMOCIÓN DE<br>$75 POR EXAMEN,<br>RAYOS-X,<br>Y LIMPIEZA.</div>

  <div class="abs location"><span>OUR LOCATION:</span><span>7815 N. Harwick Ave, Suite B, Culver City, CA 90230</span></div>
  <div class="abs map" role="img" aria-label="Street map with a pin marking the office location"></div>
  <div class="abs office-photo" role="img" aria-label="Photo of the dental office building with tile roof and palm trees"></div>
</section>

</body>
</html>
```